Business Card Design Project

This is a new division in our company. "Meridale Wellsite & Safety" This is a Oilfield Safety company. I have included our new logo. I also have given our other business card. We love double sided with lots of color. We like to stand out. Please DO NOT duplicate our other card and bring your design into it. See all attached files.
Reason: forgot to change this when I posted it.
Here is the correct information card.
www.meridalewellsitesafety.com
Dwayne@meridalewellsitesafety.com
Reason: revision for a few.
Reason: was traveling and need to review designs.
Oil and Gas industry. Masculine look.
Business

```html
<!DOCTYPE html>
<html lang="en">
<head>
<meta charset="utf-8">
<title>Meridale Wellsite &amp; Safety — Business Card</title>
<link href="https://fonts.googleapis.com/css2?family=Open+Sans:wght@400;600;700&family=Russo+One&display=swap" rel="stylesheet">
<style>
  :root {
    --page: #ecebe6;
    --green-dark: #1f7a3c;
    --green: #2e9a4c;
    --green-light: #4cbb5f;
    --white: #ffffff;
    --paper: #f2f2f2;
    --gold: #f5c518;
    --orange: #f07b22;
    --teal: #3fb8c4;
    --ink-light: #eaf7ec;
  }
  * { box-sizing: border-box; margin: 0; padding: 0; }
  html, body { width: 704px; height: 1200px; overflow: hidden; }
  body {
    background: var(--page);
    font-family: "Open Sans", Arial, sans-serif;
    position: relative;
  }
  .card {
    position: absolute;
    left: 72px;
    width: 560px;
    height: 320px;
    border-radius: 16px;
    overflow: hidden;
    box-shadow: 0 10px 26px rgba(0,0,0,.22);
  }
  .card--front { top: 130px; background: linear-gradient(160deg, var(--green-light), var(--green) 45%, var(--green-dark)); }
  .card--back { top: 730px; background: var(--paper); }

  .rig-scene {
    position: absolute; right: 0; top: 0; width: 330px; height: 220px;
    background: linear-gradient(180deg, rgba(20,80,40,.35), rgba(20,80,40,0));
  }
  .wordmark {
    font-family: "Russo One", Arial, sans-serif;
    font-weight: 400;
    color: var(--teal);
    line-height: 1.05;
    text-transform: uppercase;
    white-space: nowrap;
  }
  .card--front .wordmark { position: absolute; left: 56px; top: 96px; font-size: 34px; color: var(--white); }
  .wordmark small { display: block; font-size: .6em; }
  .tagline {
    position: absolute; right: 40px; bottom: 44px;
    color: var(--white); font-size: 20px; font-weight: 600;
  }
  .tagline em { color: var(--gold); font-style: normal; }

  .card--back .wordmark { position: absolute; left: 22px; top: 124px; font-size: 22px; }
  .band {
    position: absolute; top: 0; bottom: 0; left: 180px; width: 160px;
    background: var(--green-light);
    padding: 72px 14px 0;
  }
  .band .name { color: var(--gold); font-weight: 700; font-size: 16px; text-transform: uppercase; white-space: nowrap; }
  .band .call-label { margin-top: 104px; color: var(--orange); font-weight: 700; font-size: 14px; display: flex; align-items: center; gap: 6px; }
  .band .call-number { color: var(--gold); font-weight: 700; font-size: 15px; white-space: nowrap; }
  .contact {
    position: absolute; top: 0; bottom: 0; left: 340px; right: 0;
    background: var(--green);
    list-style: none;
    padding: 66px 10px 0 12px;
    color: var(--ink-light); font-size: 9.5px;
  }
  .contact li { display: flex; align-items: center; gap: 6px; margin-bottom: 12px; white-space: nowrap; }
  .contact svg, .call-label svg { flex: none; }
</style>
</head>
<body>

<section class="card card--front">
  <div class="rig-scene" role="img" aria-label="Faint oil rig and refinery scene"></div>
  <p class="wordmark">Meridale<small>Wellsite &amp; Safety</small></p>
  <p class="tagline">For All Your <em>Site Safety</em> Needs</p>
</section>

<section class="card card--back">
  <p class="wordmark">Meridale<small>Wellsite &amp; Safety</small></p>
  <div class="band">
    <p class="name">Dwayne Harlan</p>
    <p class="call-label">
      <svg width="14" height="14" viewBox="0 0 14 14"><rect x="1" y="1" width="12" height="12" rx="2" fill="var(--orange)"/><path d="M4 4h2v2l-1 1a5 5 0 0 0 2 2l1-1h2v2c-4 0-6-2-6-6z" fill="var(--white)"/></svg>
      CALL
    </p>
    <p class="call-number">1-800-555-0133</p>
  </div>
  <ul class="contact">
    <li><svg width="10" height="12" viewBox="0 0 10 12"><path d="M5 0a4 4 0 0 1 4 4c0 3-4 8-4 8S1 7 1 4a4 4 0 0 1 4-4z" fill="var(--orange)"/><circle cx="5" cy="4" r="1.5" fill="var(--green)"/></svg>4810 County Road 12</li>
    <li><svg width="10" height="12" viewBox="0 0 10 12"><path d="M5 0a4 4 0 0 1 4 4c0 3-4 8-4 8S1 7 1 4a4 4 0 0 1 4-4z" fill="var(--orange)"/><circle cx="5" cy="4" r="1.5" fill="var(--green)"/></svg>Brackett, TX 77590</li>
    <li><svg width="10" height="10" viewBox="0 0 10 10"><path d="M1 1h3v2.5L3 4.5a5 5 0 0 0 2.5 2.5l1-1H9v3C4.5 9 1 5.5 1 1z" fill="var(--orange)"/></svg>1-800-555-0147</li>
    <li><svg width="10" height="10" viewBox="0 0 10 10"><path d="M1 1h3v2.5L3 4.5a5 5 0 0 0 2.5 2.5l1-1H9v3C4.5 9 1 5.5 1 1z" fill="var(--orange)"/></svg>713-555-0192</li>
    <li><svg width="11" height="9" viewBox="0 0 11 9"><rect x=".5" y=".5" width="10" height="8" fill="var(--orange)"/><path d="M.5.5l5 4 5-4" stroke="var(--green)" fill="none"/></svg>Dwayne@meridalewellsitesafety.com</li>
    <li><svg width="10" height="10" viewBox="0 0 10 10"><circle cx="5" cy="5" r="4.5" fill="var(--orange)"/><path d="M.5 5h9M5 .5c-2 2.5-2 6.5 0 9M5 .5c2 2.5 2 6.5 0 9" stroke="var(--green)" stroke-width=".8" fill="none"/></svg>www.meridalewellsitesafety.com</li>
  </ul>
</section>

</body>
</html>
```